Infectious Diseases Research Laboratory Needs Business Card

We need a business card for an academic research laboratory based in Kansas City called MORVEK. The full lab name is Microbial Dose-Response/Exposure Bridging Studies Laboratory, but this does not need to be incorporated. We study novel ways to optimize the treatment of multidrug-resistant bacterial infections ("superbugs") throughout the entire biomedical research spectrum (from benchtop to bedside). The name MORVEK is not only an acronym for our lab name, but also represents our desire to make discoveries and explore the unknown (the stars, if you well). It also serves as an ode to the state of Kansas motto where we are based, ad astra per aspera ("to the stars, through difficulty").

Target Market(s)

Pharmaceutical companies, researchers

Industry/Entity Type

Pharmaceutical

Contact Information for Business Card

The business card should incorporate and complement our new logo (see uploaded files). Double-sided designs are preferred. Looking for something modern, but professional.

Font styles to use
Sans Serif

Requirements
Must have
• Double-sided. One side would ideally be a solid color incorporating logo and the other should also have the logo (smaller), but incorporate staff information.
• Color codes:
• Red: #F04C51
• Blue: #3477B5
• Gray: #808285

```html
<!DOCTYPE html>
<html lang="en">
<head>
<meta charset="utf-8">
<title>MORVEK Business Card</title>
<link href="https://fonts.googleapis.com/css2?family=Arimo:wght@400;700&display=swap" rel="stylesheet">
<style>
  :root {
    --red: #F04C51;
    --blue: #3477B5;
    --blue-deep: #2E78B7;
    --gray: #808285;
    --text: #555759;
    --white: #ffffff;
    --backdrop: #9FC3CC;
  }
  * { margin: 0; padding: 0; box-sizing: border-box; }
  html, body { width: 1200px; height: 965px; overflow: hidden; }
  body {
    background: var(--backdrop);
    font-family: "Arimo", Arial, sans-serif;
    position: relative;
  }
  .card {
    position: absolute;
    left: 275px;
    width: 703px;
    height: 388px;
    overflow: hidden;
  }
  .card-front { top: 87px; background: var(--white); }
  .card-back { top: 511px; background: var(--blue-deep); }

  .brand { position: absolute; display: flex; align-items: center; gap: 12px; }
  .brand-dot { width: 58px; height: 58px; border-radius: 50%; flex: none; }
  .brand-name { font-size: 52px; font-weight: 400; line-height: 1; letter-spacing: 1px; }
  .brand-lab { font-size: 6.2px; letter-spacing: 0.4px; text-transform: uppercase; margin-top: 4px; white-space: nowrap; }

  .card-front .brand { left: 47px; top: 34px; }
  .card-front .brand-dot { background: var(--blue); }
  .card-front .brand-name { color: var(--red); }
  .card-front .brand-lab { color: var(--gray); }

  .accent-band { position: absolute; left: 0; top: 155px; width: 100%; height: 39px; background: var(--red); }

  .contact-list { position: absolute; left: 44px; top: 231px; list-style: none; }
  .contact-list li { display: flex; align-items: center; gap: 13px; height: 21px; font-size: 17px; color: var(--text); }
  .contact-list svg { width: 16px; height: 16px; flex: none; }

  .address { position: absolute; left: 44px; top: 304px; font-size: 17px; line-height: 21px; color: var(--text); }

  .bubble-field {
    position: absolute; left: 487px; top: 254px; width: 216px; height: 134px;
    background: radial-gradient(ellipse at 60% 40%, rgba(240,76,81,0.16), rgba(52,119,181,0.10) 55%, rgba(255,255,255,0) 80%);
  }

  .staff { position: absolute; left: 499px; top: 200px; }
  .staff-name { font-size: 26px; font-weight: 700; color: var(--red); line-height: 30px; }
  .staff-role { font-size: 17px; color: var(--blue); line-height: 20px; }

  .card-back .brand { left: 50%; top: 160px; transform: translateX(-50%); }
  .card-back .brand-dot { background: var(--white); }
  .card-back .brand-name, .card-back .brand-lab { color: var(--white); }

  .back-url { position: absolute; left: 0; width: 100%; top: 347px; text-align: center; font-size: 19px; color: var(--white); }
</style>
</head>
<body>
  <section class="card card-front">
    <div class="brand">
      <span class="brand-dot"></span>
      <div>
        <div class="brand-name">MORVEK</div>
        <div class="brand-lab">Microbial Dose-Response/Exposure Bridging Studies Laboratory</div>
      </div>
    </div>

    <div class="accent-band"></div>

    <ul class="contact-list">
      <li>
        <svg viewBox="0 0 16 16"><path d="M4 2 L6.5 5 L5 6.5 Q6.5 9.5 9.5 11 L11 9.5 L14 12 L12.5 14 Q6 13.5 2 4 Z" fill="none" stroke="#F04C51" stroke-width="1.5" stroke-linejoin="round"/></svg>
        <span>001 555 0148</span>
      </li>
      <li>
        <svg viewBox="0 0 16 16"><rect x="1.5" y="3.5" width="13" height="9" fill="#F04C51"/><path d="M1.5 3.5 L8 9 L14.5 3.5" fill="none" stroke="#fff" stroke-width="1.2"/></svg>
        <span>info@morvek.org</span>
      </li>
      <li>
        <svg viewBox="0 0 16 16"><g fill="none" stroke="#F04C51" stroke-width="1.3"><circle cx="8" cy="8" r="6.3"/><ellipse cx="8" cy="8" rx="2.8" ry="6.3"/><line x1="1.7" y1="8" x2="14.3" y2="8"/></g></svg>
        <span>www.morvek.org</span>
      </li>
    </ul>

    <p class="address">4127 Harlow Street, Suite 210<br>Kansas City, KS 66160</p>

    <div class="bubble-field" role="img" aria-label="Faint scattered red and blue circles decoration"></div>

    <div class="staff">
      <div class="staff-name">Dalen Pryce</div>
      <div class="staff-role">Vice President</div>
    </div>
  </section>

  <section class="card card-back">
    <div class="brand">
      <span class="brand-dot"></span>
      <div>
        <div class="brand-name">MORVEK</div>
        <div class="brand-lab">Microbial Dose-Response/Exposure Bridging Studies Laboratory</div>
      </div>
    </div>
    <div class="back-url">www.morvek.org</div>
  </section>
</body>
</html>
```